Business Card Design Project

Crestline Vein Center

Dr Tomas Venrick M.D, F.R.C.S
Vascular and Vein Surgery

47-18 Pellham Avenue, Suite 314
Astoria
NY 11287

212-555-0147
718-555-0193
www.crestlinecare.us back of the card for scheduled appointments up to 5 appointment dates

Target Market(s)

Male and Female patients from 25 onwards with spider veins or varicose veins

Industry/Entity Type

Business

Font styles to use
Serif

Colors
86cae6
85abd2
0456a4

Requirements
Must have
• Modern Sophisticated design using light blue and grey text
Should not have
• hearts or flowers

```html
<!DOCTYPE html>
<html lang="en">
<head>
<meta charset="utf-8">
<title>Crestline Vein Center – Business Card</title>
<link rel="stylesheet" href="https://fonts.googleapis.com/css2?family=Bebas+Neue&family=Zilla+Slab:wght@300;400&display=swap">
<style>
  :root {
    --sky: #86cae6;
    --sky-deep: #7fc3e3;
    --vein-blue: #85abd2;
    --frame-grey: #e6e8eb;
    --credential-grey: #e1e3e8;
    --white: #ffffff;
  }
  * { margin: 0; padding: 0; box-sizing: border-box; }
  html, body { width: 1019px; height: 1200px; overflow: hidden; background: var(--sky); }
  .card { position: relative; width: 1019px; height: 1200px; background: var(--sky); overflow: hidden; }

  .hero { position: absolute; left: 0; top: 0; width: 1019px; height: 582px; }
  .hero-texture { position: absolute; inset: 0; }

  .title-frame {
    position: absolute; left: 152px; top: 107px; width: 715px; height: 369px;
    border: 19px solid var(--frame-grey);
  }
  .brand-name, .brand-sub {
    position: absolute; left: 215px; font-family: "Bebas Neue", sans-serif;
    color: var(--white); line-height: 1; white-space: nowrap;
  }
  .brand-name { top: 178px; font-size: 160px; letter-spacing: 1px; }
  .brand-sub { top: 322px; font-size: 129px; }

  .divider-band { position: absolute; left: 0; top: 582px; width: 1019px; height: 34px; background: var(--white); }

  .doctor-name {
    position: absolute; left: 53px; top: 672px; font-family: "Bebas Neue", sans-serif;
    font-size: 76px; line-height: 1; color: var(--white); white-space: nowrap;
  }
  .credentials {
    position: absolute; left: 53px; top: 758px; font-family: "Bebas Neue", sans-serif;
    font-size: 54px; line-height: 1; color: var(--credential-grey); white-space: nowrap;
  }
  .credentials .sep { color: var(--vein-blue); margin: 0 10px; }
  .rule { position: absolute; left: 53px; top: 825px; width: 695px; height: 3px; background: var(--vein-blue); }

  .contact { position: absolute; left: 159px; font-family: "Zilla Slab", serif; font-weight: 300;
    font-size: 36px; line-height: 44px; color: var(--white); white-space: nowrap; letter-spacing: 0.5px; }
  .contact.address { top: 872px; }
  .contact.phones { top: 982px; }
  .contact.web { top: 1107px; }

  .icon { position: absolute; }
  .icon.pin { left: 64px; top: 876px; }
  .icon.phone { left: 66px; top: 990px; }
  .icon.globe { left: 52px; top: 1096px; }
</style>
</head>
<body>
<div class="card">
  <div class="hero">
    <svg class="hero-texture" width="1019" height="582" role="img" aria-label="Faint branching vein pattern across the light blue header">
      <defs>
        <radialGradient id="veinHaze" cx="0.5" cy="0.45" r="0.75">
          <stop offset="0" stop-color="#86cae6"/>
          <stop offset="1" stop-color="#82bde3"/>
        </radialGradient>
      </defs>
      <rect width="1019" height="582" fill="url(#veinHaze)"/>
    </svg>
    <div class="title-frame"></div>
    <div class="brand-name">CRESTLINE</div>
    <div class="brand-sub">VEIN CENTER</div>
  </div>

  <div class="divider-band"></div>

  <div class="doctor-name">DR TOMAS VENRICK</div>
  <div class="credentials">M.D, F.R.C.S<span class="sep">|</span>VASCULAR AND VEIN SURGERY</div>
  <div class="rule"></div>

  <svg class="icon pin" width="44" height="66" viewBox="0 0 44 66" aria-hidden="true">
    <path d="M22 0C9.8 0 0 9.6 0 21.5 0 36 22 66 22 66S44 36 44 21.5C44 9.6 34.2 0 22 0Z" fill="var(--vein-blue)"/>
    <circle cx="22" cy="21" r="9" fill="var(--sky)"/>
  </svg>
  <div class="contact address">47-18 Pellham Avenue, Suite 314<br>Astoria,NY 11287</div>

  <svg class="icon phone" width="40" height="66" viewBox="0 0 40 66" aria-hidden="true">
    <rect x="0" y="0" width="40" height="66" rx="6" fill="var(--vein-blue)"/>
    <rect x="5" y="8" width="30" height="44" fill="var(--sky)"/>
    <circle cx="20" cy="59" r="3" fill="var(--sky)"/>
  </svg>
  <div class="contact phones">(212) 555 0147<br>(718) 555 0193</div>

  <svg class="icon globe" width="66" height="66" viewBox="0 0 66 66" aria-hidden="true">
    <circle cx="33" cy="33" r="33" fill="var(--vein-blue)"/>
    <g fill="none" stroke="var(--sky)" stroke-width="3">
      <ellipse cx="33" cy="33" rx="14" ry="30"/>
      <line x1="3" y1="33" x2="63" y2="33"/>
      <path d="M8 18H58M8 48H58"/>
    </g>
  </svg>
  <div class="contact web">www.crestlinecare.us</div>
</div>
</body>
</html>
```